Corvath Partners is a boutique consultancy focused on CXO-level advisory on strategy, operations, and organization in the Consumer Packaged Goods and Retail sector.

Our typical clients are senior level executives (Typically SVP level or higher), who hire us to help solve strategic business challenges. Our consultants are typically charged out at very high rates (Typically $2,000 - $3,000 per day), therefore, our business cards need to convey a high end, classy, yet professional image, consistent with high value strategic consulting.

We would like to see designs and colors that convey excellence, competence, and growth.

Our name 'Corvath' is derived from the Native American name of Mt. McKinley, the highest peak in North America. We would like to have a logo on our business card, that is simple yet conveys the aspirational nature of what we offer, i.e enabling the achievement of high performance.

Boutique

Corvath Partners, LLC
4718 Brennock Avenue Northwest, Suite 640
Washington, District of Columbia, 20093
United States
Mobile: +1 202 555 0143
elira.voss@corvathpartnersllc.com

```html
<!DOCTYPE html>
<html lang="en">
<head>
<meta charset="utf-8">
<title>Corvath Partners, LLC — Business Card</title>
<link rel="stylesheet" href="https://fonts.googleapis.com/css2?family=Tinos:wght@700&family=Noto+Sans:wght@400&display=swap">
<style>
  :root {
    --page-bg: #eeeff1;
    --card-white: #ffffff;
    --panel-blue: #22a4d2;
    --panel-blue-light: #36b5dc;
    --text-light: #ffffff;
    --shadow: rgba(0, 0, 0, 0.18);
  }
  * { margin: 0; padding: 0; box-sizing: border-box; }
  html, body {
    width: 1200px;
    height: 864px;
    overflow: hidden;
    background: var(--page-bg);
  }
  .card {
    position: absolute;
    left: 100px;
    top: 147px;
    width: 1000px;
    height: 570px;
    display: flex;
    background: var(--card-white);
    box-shadow: 0 10px 30px var(--shadow);
  }
  .brand-side {
    width: 40%;
    position: relative;
  }
  .brand-name {
    position: absolute;
    left: 0;
    right: 0;
    top: 318px;
    text-align: center;
    font-family: "Noto Sans", "Segoe UI", sans-serif;
    font-weight: 400;
    font-size: 30px;
    color: var(--panel-blue);
    white-space: nowrap;
  }
  .info-side {
    width: 60%;
    background: linear-gradient(160deg, var(--panel-blue-light), var(--panel-blue) 60%);
    color: var(--text-light);
    padding: 76px 40px 0 40px;
    position: relative;
  }
  .employee-name {
    font-family: "Tinos", "Times New Roman", serif;
    font-weight: 700;
    font-size: 44px;
    line-height: 1;
  }
  .employee-role {
    font-family: "Noto Sans", "Segoe UI", sans-serif;
    font-size: 21px;
    margin-top: 6px;
  }
  .contact-list {
    list-style: none;
    position: absolute;
    left: 40px;
    top: 286px;
    font-family: "Noto Sans", "Segoe UI", sans-serif;
    font-size: 24px;
    line-height: 1.25;
  }
  .contact-item {
    display: flex;
    align-items: flex-start;
    margin-bottom: 26px;
  }
  .contact-icon {
    width: 24px;
    height: 24px;
    flex: none;
    margin: 6px 40px 0 0;
    fill: var(--text-light);
  }
</style>
</head>
<body>
  <div class="card">
    <div class="brand-side">
      <span class="brand-name">Corvath Partners, LLC</span>
    </div>
    <div class="info-side">
      <h1 class="employee-name">Employee Name</h1>
      <p class="employee-role">Director</p>
      <ul class="contact-list">
        <li class="contact-item">
          <svg class="contact-icon" viewBox="0 0 24 24" aria-hidden="true"><path d="M6.6 2.5l3 3.2-1.8 2.6c1.2 2.7 3.3 4.9 6 6.1l2.6-1.8 3.2 3-1.6 3.6C10.4 19 5 13.6 3 5.4z"/></svg>
          <span>+1 202 555 0143</span>
        </li>
        <li class="contact-item">
          <svg class="contact-icon" viewBox="0 0 24 24" aria-hidden="true"><path d="M2 5h20v14H2z M3.5 6.5v.6l8.5 6 8.5-6v-.6z" fill-rule="evenodd"/></svg>
          <span>elira.voss@corvathpartnersllc.com</span>
        </li>
        <li class="contact-item">
          <svg class="contact-icon" viewBox="0 0 24 24" aria-hidden="true"><path d="M12 2.5l10 9h-3V21h-5v-6h-4v6H5v-9.5H2z"/></svg>
          <span>4718 Brennock Avenue Northwest,<br>Suite 640 Washington,<br>District of Columbia,<br>20093 United States</span>
        </li>
      </ul>
    </div>
  </div>
</body>
</html>
```